Redesign of page from emergency manual

Please redesign this PDF to look better. Please don't include any stock photos. It must be legible. Making some words bold is probably a good idea.

Here are some things I like :

https://tarrowbooks.com.au/collections/frontpage/products/the-plk-v2-ebook

https://img-cd.vostramediafiles.com/qa-ejkwPLOTYY_SuCKbZNu411Qwgjv8YssPxEdzXN93hDkSRjLXK8WmfgbmrJW4ZZ3yUPK=w1052-h592-rw

```html
<!DOCTYPE html>
<html lang="en">
<head>
<meta charset="utf-8">
<title>Hypertension, Acute – Variation 2</title>
<link href="https://fonts.googleapis.com/css2?family=Poppins:ital,wght@0,300;0,400;0,500;0,600;0,700;0,800;1,400;1,500;1,700&display=swap" rel="stylesheet">
<style>
  :root {
    --cyan: #62e6f7;
    --ink: #151515;
    --frame-red: #e62020;
    --row-light: #f4f4f4;
    --row-dark: #e6e6e6;
    --table-line: #555555;
    --soft-line: #bbbbbb;
    --paper: #ffffff;
  }
  * { box-sizing: border-box; margin: 0; padding: 0; }
  html, body { width: 1200px; height: 1200px; overflow: hidden; background: var(--paper); }
  body { position: relative; font-family: 'Poppins', sans-serif; color: var(--ink); }

  .board-title {
    position: absolute; top: 38px; left: 0; width: 1200px; text-align: center;
    font-weight: 400; font-size: 68px; line-height: 1;
  }
  .page {
    position: absolute; left: 10px; top: 136px; width: 1178px; height: 927px;
    border: 2px solid var(--frame-red); background: var(--paper);
  }
  .running-head {
    position: absolute; left: 48px; top: 24px; font-size: 42px; font-weight: 400; line-height: 1; white-space: nowrap;
  }
  .running-rule { position: absolute; left: 494px; top: 43px; width: 494px; height: 2px; background: var(--ink); }
  .page-number {
    position: absolute; left: 1032px; top: -1px; width: 89px; height: 84px; background: var(--cyan);
    color: #fff; font-weight: 800; font-size: 50px; text-align: center; line-height: 86px;
  }
  .head-band { position: absolute; left: 0; right: 0; top: 82px; height: 5px; background: var(--cyan); }

  .page-title {
    position: absolute; left: 50px; top: 122px; font-weight: 800; font-size: 49px; line-height: 1; white-space: nowrap;
  }
  .title-bar {
    position: absolute; left: 50px; top: 177px; width: 207px; height: 15px; background: var(--cyan);
    box-shadow: 4px 4px 6px rgba(0,0,0,.18);
  }
  .definition {
    position: absolute; left: 682px; top: 123px; width: 459px; height: 75px;
    border: 5px solid var(--cyan); border-radius: 20px;
    display: flex; align-items: center; justify-content: center; text-align: center;
    color: var(--cyan); font-weight: 800; font-size: 17px; line-height: 15px; letter-spacing: .2px;
  }

  .intro { position: absolute; left: 48px; top: 216px; width: 550px; font-size: 22px; line-height: 27px; }
  .step-num { position: absolute; font-weight: 700; font-size: 42px; line-height: 1; }
  .step-text { position: absolute; font-size: 22px; line-height: 27px; white-space: nowrap; }
  .n1 { left: 48px; top: 308px; }
  .t1 { left: 88px; top: 322px; }
  .n2 { left: 48px; top: 389px; }
  .t2 { left: 88px; top: 402px; }
  .t2-sub { left: 81px; top: 429px; }

  .bp-table {
    position: absolute; left: 670px; top: 240px; width: 467px; border-collapse: separate; border-spacing: 0;
    table-layout: fixed;
    border: 2px solid var(--table-line); border-radius: 8px; overflow: hidden; box-shadow: 3px 4px 6px rgba(0,0,0,.18);
    font-size: 20px; text-align: center;
  }
  .bp-table .bp-head th {
    background: var(--cyan); height: 38px; font-weight: 600; font-size: 19px; letter-spacing: .2px;
  }
  .bp-table th, .bp-table td { border-bottom: 1.5px solid var(--soft-line); }
  .bp-table .col-head th { height: 45px; font-weight: 600; font-size: 20px; }
  .bp-table td { height: 35px; font-weight: 400; }
  .bp-table tr:last-child td { border-bottom: none; }
  .bp-table .col-head th + th, .bp-table td + td { border-left: 1.5px solid var(--soft-line); }

  .drug-table {
    position: absolute; left: 47px; top: 483px; width: 1096px; border-collapse: separate; border-spacing: 0;
    table-layout: fixed;
    border: 2px solid var(--table-line); border-radius: 20px; overflow: hidden; box-shadow: 3px 5px 8px rgba(0,0,0,.2);
    font-size: 19.5px; line-height: 23px;
  }
  .drug-table th {
    background: var(--cyan); height: 45px; font-weight: 700; font-size: 22px; border-bottom: 2px solid var(--table-line);
  }
  .drug-table th + th, .drug-table td + td { border-left: 2px solid var(--table-line); }
  .drug-table td { vertical-align: top; border-bottom: 2px solid var(--table-line); padding-top: 8px; }
  .drug-table tr:last-child td { border-bottom: none; }
  .drug-table .action { padding-left: 25px; padding-right: 0; font-size: 20px; white-space: nowrap; }
  .drug-table .drugs { padding-left: 16px; padding-right: 6px; }
  .drug-table tr.light td { background: var(--row-light); }
  .drug-table tr.dark td { background: var(--row-dark); }
  .drug-table .r1 td { height: 76px; }
  .drug-table .r2 td { height: 79px; }
  .drug-table .r3 td { height: 78px; }
  .drug-table .r4 td { height: 38px; padding-top: 6px; }
  .drug-list { list-style: none; }
  .drug-list li { position: relative; padding-left: 21px; margin-bottom: 9px; white-space: nowrap; }
  .drug-list li::before {
    content: ""; position: absolute; left: 0; top: 8px; width: 7px; height: 7px; background: var(--ink);
  }
  .r2 .drug-list li { margin-bottom: 15px; }

  .footnote {
    position: absolute; left: 52px; top: 828px; padding-left: 14px; white-space: nowrap;
    font-style: italic; font-weight: 500; font-size: 19.8px; line-height: 26px;
  }
  .footnote-mark { position: absolute; left: 0; top: 1px; font-style: normal; font-size: 16px; }
  .footnote strong { font-weight: 700; }

  .design-note {
    position: absolute; left: 78px; top: 1084px; white-space: nowrap;
    font-weight: 300; font-size: 22.4px; line-height: 27.5px;
  }
  .design-note .accent { color: var(--frame-red); }
</style>
</head>
<body>
  <h1 class="board-title">VARIATION 2</h1>

  <section class="page">
    <div class="running-head">Hypertension, Acute</div>
    <div class="running-rule"></div>
    <div class="page-number">12</div>
    <div class="head-band"></div>

    <h2 class="page-title">HYPERTENSION, ACUTE</h2>
    <div class="title-bar"></div>

    <div class="definition">SUSTAINED HIGH BLOOD PRESSURE REFRACTORY<br>TO TREATING REVERSIBLE CAUSES</div>

    <p class="intro">In pediatrics, hypertension is almost always<br>treated by addressing likely causes such as light<br>anesthesia or measurement error:</p>

    <span class="step-num n1">1.</span>
    <span class="step-text t1">Ensure correct BP cuff size: cuff bladder<br>width ~ 40% of limb circumference.</span>
    <span class="step-num n2">2.</span>
    <span class="step-text t2">Ensure arterial line transducer is at level of heart</span>
    <span class="step-text t2-sub">- Consider placing arterial line if not already present</span>

    <table class="bp-table">
      <colgroup><col style="width:144px"><col style="width:162px"><col></colgroup>
      <tr class="bp-head"><th colspan="3">HYPERTENSIVE BLOOD PRESSURE RANGE*</th></tr>
      <tr class="col-head"><th>Age (yr)</th><th>Systolic</th><th>Diastolic</th></tr>
      <tr><td>newborn</td><td>&gt;97</td><td>&gt;70</td></tr>
      <tr><td>1 -3</td><td>&gt;105</td><td>&gt;61</td></tr>
      <tr><td>4-12</td><td>&gt;113</td><td>&gt;86</td></tr>
    </table>

    <table class="drug-table">
      <colgroup><col style="width:247px"><col></colgroup>
      <tr><th>ACTION</th><th>DRUG (IV DOSING)</th></tr>
      <tr class="light r1">
        <td class="action">Direct smooth muscle<br>relaxation</td>
        <td class="drugs"><ul class="drug-list">
          <li>Sodium nitroprusside 0.5 -10 &nbsp;MICROgrams/kg/min</li>
          <li>HydrALAZINE &nbsp; 0.1 -0.2 mg/kg (adult dose 5 -10 mg)</li>
        </ul></td>
      </tr>
      <tr class="dark r2">
        <td class="action">β-Adrenergic<br>blockade</td>
        <td class="drugs"><ul class="drug-list">
          <li>Esmolol 100 -500 MICROgrams/kg over 5 min, then 25-300 MICROgrams/kg/min</li>
          <li>Labetalol (also α effect) 0.2 -1 mg/kg q 10 min; 0.4 -3 mg/kg/ hour (infusion)</li>
        </ul></td>
      </tr>
      <tr class="light r3">
        <td class="action">Calcium channel<br>blockade</td>
        <td class="drugs"><ul class="drug-list">
          <li>niCARdapine &nbsp;0.5 -5 MICROgrams/kg/min</li>
          <li>Clevidipine 0.5 -3.5 MICROgrams/kg/min</li>
        </ul></td>
      </tr>
      <tr class="dark r4">
        <td class="action">D1 -dopamine agonist</td>
        <td class="drugs"><ul class="drug-list">
          <li>Fenoldopam 0.2 -0.8 MICROgrams/kg/min</li>
        </ul></td>
      </tr>
    </table>

    <p class="footnote"><span class="footnote-mark">*</span>Anti-hypertensive drugs are almost never needed for routine pediatric cases. These medications are<br>used almost exclusively for specialized cardiac, neurosurgical, or endocrine (pheochromocytoma) cases.<br><strong>Consult an expert before use.</strong> Rule-out increased ICP.</p>
  </section>

  <p class="design-note">For variation 2 &nbsp;i went creative and thought out of the box to give some extra edsign elements<br>such as shadow, bold headings and typography. I also change the font to look more professional,<br>easy and comfortable for readers eye. <span class="accent">Red Line Show Original PDf page size.</span></p>
</body>
</html>
```